Bold Cover needed for a book on Workplace Bullying

I need a book cover design for a book titled, “Iron Silence?” The book recounts my story of bullying in the workplace. It also includes chapters on how readers can minimize/stop workplace bullying, write an effective complaint, and ensure their own mental wellbeing.
I am looking for a bold design using red and black, and possibly distressed lettering. The covers of other books dealing with this subject do not reflect my vision. They are often too childish or look too academic. This book needs to stress the serious nature of a toxic workplace, while appealing to readers experiencing a similar situation. I’d like the cover to reflect the mental anguish associated with workplace bullying (hence the distressed lettering).
I have included a cover that appeals to me (although the coloring is wrong). That said, I am also very happy (and excited) to see your creative input!
On the cover, it should have the following:
Title: Iron Silence?
Subtitle: How the Harbour Works Department Condones Bullying & Ruins Lives
Author: Owen Frick
Other relevant details:
Book size: 5.5” x 8.5”
Back cover will have a blurb, author picture/short bio, and barcode
The blurb on the back cover reads:
Undermining, intimidation and threats
Despite the Department of Harbour Works allegedly holding a zero tolerance for bullying, these behaviours were an everyday occurrence in at least one workplace. Even after a decade of complaints, numerous witnesses and physical proof, the department failed to act. Instead, they looked the other way, allowing one powerful and well-connected individual to end careers and ruin lives.
After being targeted, one teacher resolved to put an end to the abuse experienced by more than fifty employees. His startling story reveals the relentless bullying, mental health ramifications, and insidious tactics used to cover up the corrosive behaviour.
Those who have experienced a toxic workplace will also find much needed support and guidance, intended to minimise suffering and detail a clear way forward. Chapters include dealing with bullying in the workplace, how to lodge a successful complaint, and how to stay sane during any potential legal action.

```html
<!DOCTYPE html>
<html lang="en">
<head>
<meta charset="utf-8">
<title>Iron Silence? – Book Cover</title>
<link href="https://fonts.googleapis.com/css2?family=Open+Sans:wght@600;700;800&family=Playfair+Display:wght@400&family=Great+Vibes&family=Rubik+Dirt&display=swap" rel="stylesheet">
<style>
  :root {
    --stage: #2b2b2b;
    --ink: #0a0a0a;
    --red: #ee1c1c;
    --red-bright: #ff2a2a;
    --board: #050505;
  }
  * { box-sizing: border-box; margin: 0; padding: 0; }
  html, body { width: 1200px; height: 960px; overflow: hidden; background: var(--stage); }
  .spread {
    position: absolute; left: 57px; top: 80px;
    display: flex; height: 800px;
  }
  /* Back cover */
  .back-cover {
    width: 518px; height: 800px; background: var(--board);
    color: var(--red); text-align: center;
    padding: 70px 40px 0;
    font-family: "Playfair Display", serif;
  }
  .back-cover .tagline {
    font-family: "Great Vibes", cursive; font-size: 84px; line-height: 1;
    margin-bottom: 60px; font-weight: 400;
  }
  .back-cover .blurb p { font-size: 16px; line-height: 1.3; margin-bottom: 44px; }
  /* Spine */
  .spine {
    width: 50px; height: 800px; background: var(--ink); position: relative;
  }
  .spine .author {
    position: absolute; left: 50%; top: 470px;
    transform: translate(-50%, -50%) rotate(-90deg);
    white-space: nowrap;
    font-family: "Playfair Display", serif; font-size: 30px; letter-spacing: 2px;
    color: var(--red);
  }
  /* Front cover */
  .front-cover {
    width: 518px; height: 800px; position: relative; overflow: hidden;
    background: linear-gradient(160deg, var(--red-bright), var(--red) 60%);
  }
  .title-initial {
    position: absolute; left: 30px; top: -60px;
    font-family: "Open Sans", sans-serif; font-weight: 800;
    font-size: 560px; line-height: 1; color: var(--ink);
  }
  .title-rest {
    position: absolute; left: 200px; top: 360px;
    font-family: "Open Sans", sans-serif; font-weight: 700;
    font-size: 104px; line-height: 1; color: var(--ink); letter-spacing: -2px;
  }
  .dark-block {
    position: absolute; left: 259px; top: 480px; width: 259px; height: 320px;
    background: var(--ink);
  }
  .title-word {
    position: absolute; left: 478px; top: 470px;
    transform-origin: left top; transform: rotate(90deg);
    font-family: "Rubik Dirt", sans-serif; font-size: 60px; line-height: 1;
    color: var(--red); white-space: nowrap;
  }
  .title-mark {
    position: absolute; left: 290px; top: 485px;
    font-family: "Rubik Dirt", sans-serif; font-size: 230px; line-height: 1;
    color: var(--red);
  }
  .profiles {
    position: absolute; left: 40px; top: 530px; width: 230px; height: 190px;
    background: linear-gradient(180deg, #111, var(--ink));
    border-radius: 90px 90px 0 0;
  }
  .subtitle {
    position: absolute; left: 0; right: 0; bottom: 14px;
    font-family: "Open Sans", sans-serif; font-weight: 700;
    font-size: 17px; line-height: 1.15; text-align: center;
    color: var(--ink); text-transform: uppercase;
  }
  .subtitle-band {
    position: absolute; left: 0; right: 0; bottom: 0; height: 62px;
    background: var(--red);
  }
</style>
</head>
<body>
  <div class="spread">
    <section class="back-cover">
      <h2 class="tagline">Free</h2>
      <div class="blurb">
        <p>Lorem ipsum dolor sit amet, consectetur adipiscing elit, sed do eiusmod tempor incididunt ut labore et dolore magna aliqua. Quis ipsum suspendisse ultrices gravida. Risus commodo viverra maecenas accumsan lacus vel facilisis. Lore incididunt ut labore et dolore magna aliqua. Quis ipsum suspendisse ultrices gravida. Risus commodo viverra maecenas accumsan lacus vel facilisis.</p>
        <p>Lorem ipsum dolor sit amet, consectetur adipiscing elit, sed do eiusmod tempor incididunt ut labore et dolore magna aliqua. Quis ipsum suspendisse ultrices gravida. Risus commodo viverra maecenas accumsan lacus vel facilisis.</p>
        <p>Lorem ipsum dolor sit amet, consectetur adipiscing elit, sed do eiusmod tempor incididunt ut labore et dolore magna aliqua. Quis ipsum suspendisse ultrices gravida. Risus commodo viverra maecenas accumsan lacus vel facilisis. Lorem ipsum dolor sit amet, consectetur adipiscing elit, sed do eiusmod tempor incididunt ut labore et dolore magna aliqua.</p>
        <p>Lorem ipsum dolor sit ae ultrices gravida. Risus commodo viverra maecenas accumsan lacus vel facilisis.</p>
      </div>
    </section>
    <div class="spine">
      <span class="author">OWEN FRICK</span>
    </div>
    <section class="front-cover">
      <div class="dark-block"></div>
      <div class="profiles" role="img" aria-label="Black silhouettes of two head profiles facing each other"></div>
      <h1 class="title">
        <span class="title-initial">I</span>
        <span class="title-rest">RON</span>
        <span class="title-word">SILENCE</span>
        <span class="title-mark">?</span>
      </h1>
      <div class="subtitle-band"></div>
      <p class="subtitle">How the Harbour Works Department Condones<br>Bullying &amp; Ruins Lives</p>
    </section>
  </div>
</body>
</html>
```